Website design for luxury private hair salon

I'm looking for someone to use my Logo and build me a website for my webpage www.lunetresses.com.au (You can have a look at it as it has every detail I need included on it already), however I want a fresh new appearance and it to look and feel super stylish.

I am thinking colours in black, with silver or white, beautiful hair images like the ones you'll see on the current webpage - the price list as per what you already see.

I will include a copy of my biz card on here, so you can see the feel of the card, and design a website with a similar feel. It is matt black with a foil silver.

Modern, but classic and fresh. I will also need you to be able to publish it to my URL for me as I have no idea how to do this. I need it up and running pronto!

The website will need to be able to be read clearly on all devices incluing smart phones and ipads. The URL is currently registered and hosted by Nimbo Vault

Thinking a Home Page - large logo etc and write up on who and what we offer
Services/Price List page - as per the price list on my current webpage
Contact Page - with a built in contact form.

Target Market(s)

Middle aged, fashionable, stylish women and men who enjoy luxury hair care and styling in an upmarket location.

Industry/Entity Type

Hair And Beauty

Number of Pages Required

3 page

Font styles to use
Other font styles liked:
• see my images for my current logo

Colors
000000
b2b2b2
a54499

Requirements
Must have
• Style
• Fast turnaround
• Be viewable on all devices, PC, ipads, smart phones
• Designer able to upload it so its a running website for me to my URL
Nice to have
• Just a really feminine, stylish website which is easy to read and shows some beautiful images of perfect hair
Should not have
• Browns, reds or orange colours.

```html
<!DOCTYPE html>
<html lang="en">
<head>
<meta charset="utf-8">
<title>Lune hair &amp; body</title>
<link href="https://fonts.googleapis.com/css2?family=Lato:wght@300;400;700&family=Open+Sans:wght@600&family=Ubuntu:wght@400;500&family=Montserrat:wght@700&display=swap" rel="stylesheet">
<style>
:root{
  --accent:#a54499;
  --accent-bright:#c455b7;
  --button:#b545a8;
  --ink:#1a1a1a;
  --text:#3c3c3c;
  --muted:#6e6e6e;
  --rule:#c9c9c9;
  --white:#ffffff;
  --plum:#540a4d;
}
*{margin:0;padding:0;box-sizing:border-box}
html,body{width:1079px;height:1200px;overflow:hidden;background:var(--white)}
body{position:relative;font-family:'Lato',sans-serif;color:var(--text)}
a{text-decoration:none}

.hero{position:absolute;left:0;top:0;width:1079px;height:519px;overflow:hidden}
.hero-image{position:absolute;inset:0;
  background:
    radial-gradient(ellipse 260px 330px at 880px 230px,#8f9bb0 0%,rgba(120,132,155,.6) 45%,rgba(40,52,78,0) 100%),
    radial-gradient(ellipse 200px 90px at 740px 310px,rgba(210,90,130,.55),rgba(210,90,130,0) 100%),
    radial-gradient(ellipse 420px 300px at 80px 120px,#8f9aaa 0%,rgba(90,104,126,.4) 60%,rgba(40,52,78,0) 100%),
    linear-gradient(180deg,#3c4b66 0%,#2d3b57 60%,#263350 100%)}

.nav{position:absolute;top:65px;left:0;width:100%;height:16px}
.nav a{position:absolute;top:0;font-size:11px;color:var(--white);letter-spacing:.1px;white-space:nowrap}
.nav a.is-active{color:var(--accent-bright)}
.brand{position:absolute;left:456px;top:34px;width:160px;text-align:center;color:var(--white)}
.brand-name{display:block;font-family:'Lato',sans-serif;font-weight:300;font-size:46px;line-height:48px;letter-spacing:1px}
.brand-sub{display:block;font-family:'Lato',sans-serif;font-weight:300;font-size:12px;letter-spacing:1.5px;margin-top:-2px}

.hero-title{position:absolute;top:220px;left:0;width:1079px;text-align:center;font-weight:300;font-size:40px;letter-spacing:4px;color:var(--white)}
.hero-cta{position:absolute;left:483px;top:299px;width:114px;height:27px;background:var(--button);color:var(--white);font-family:'Montserrat',sans-serif;font-weight:700;font-size:10.5px;letter-spacing:2.4px;text-align:center;line-height:27px}

.info-bar{position:absolute;left:71px;top:415px;width:937px;height:70px;background:rgba(160,170,185,.35)}
.info{position:absolute;top:0;height:70px;display:flex;align-items:center;gap:10px}
.info svg{flex:none}
.info-title{font-weight:700;font-size:11.5px;color:var(--white);line-height:17px}
.info-detail{font-size:11px;color:var(--white);line-height:17px}

.services{position:absolute;top:557px;left:0;width:1079px}
.service{position:absolute;top:0;width:136px;text-align:center}
.service-image{width:136px;height:136px;background:linear-gradient(160deg,#e6e6e6,#a9a9a9)}
.service-image.is-colour{background:linear-gradient(160deg,#f1ece8 0%,#d86a35 55%,#efe7e2 100%)}
.service-label{display:block;margin-top:10px;font-family:'Open Sans',sans-serif;font-weight:600;font-size:11.5px;color:var(--muted)}
.service.is-current .service-label{color:var(--text)}

.price-list{position:absolute;top:750px;width:428px}
.price-list.left{left:111px}
.price-list.right{left:568px;width:408px}
.price-head{position:absolute;top:0;font-family:'Ubuntu',sans-serif;font-size:9px;color:var(--ink);white-space:nowrap}
.price-row{position:absolute;left:0;width:100%;height:20px;font-family:'Ubuntu',sans-serif}
.price-row::before{content:"";position:absolute;left:0;right:0;bottom:3px;border-bottom:1px dashed var(--rule)}
.price-row .name,.price-row .price{position:absolute;bottom:0;background:var(--white);line-height:16px}
.price-row .name{left:0;font-size:12.5px;color:var(--text);padding-right:2px}
.price-row .price{font-size:15px;font-weight:500;color:var(--accent);padding:0 1px;transform:translateX(-50%)}

.testimonial{position:absolute;top:1122px;left:0;width:1079px;height:78px}
.testimonial-image{position:absolute;left:0;top:0;width:540px;height:78px;background:linear-gradient(90deg,#3c4a2f 0%,#6d5a6a 45%,#3f2b45 70%,#a79aa5 100%)}
.testimonial-panel{position:absolute;left:540px;top:0;width:539px;height:78px;background:var(--plum)}
</style>
</head>
<body>

<header class="hero">
  <div class="hero-image" role="img" aria-label="Close-up beauty portrait of a woman with sleek dark hair and bold pink lips"></div>

  <nav class="nav">
    <a class="is-active" style="left:181px" href="#">HOME</a>
    <a style="left:254px" href="#">ABOUT US</a>
    <a style="left:347px" href="#">SERVICES</a>
    <a style="left:666px" href="#">BOOK</a>
    <a style="left:738px" href="#">PRICE LIST</a>
    <a style="left:832px" href="#">CONTACT US</a>
  </nav>

  <div class="brand">
    <span class="brand-name">Lune</span>
    <span class="brand-sub">hair &amp; body</span>
  </div>

  <h1 class="hero-title">FROM HEAD TO TOE</h1>
  <a class="hero-cta" href="#">READ MORE</a>

  <div class="info-bar">
    <div class="info" style="left:30px">
      <svg width="38" height="38" viewBox="0 0 38 38" fill="none" stroke="#c94fc0" stroke-width="2.2"><circle cx="19" cy="19" r="17"/><path d="M17 9v11l8 6" stroke-linecap="round"/></svg>
      <div><div class="info-title">OPANING HOUR</div><div class="info-detail">MONDAY - FRIDAY : 09:00 - 22:00</div></div>
    </div>
    <div class="info" style="left:342px">
      <svg width="36" height="36" viewBox="0 0 36 36" fill="none" stroke="#c94fc0" stroke-width="2.2" stroke-linejoin="round"><path d="M3 18 18 4l15 14"/><path d="M7 15v18h22V15"/><path d="M14 33v-9h8v9"/></svg>
      <div><div class="info-title">OUR LOCATION</div><div class="info-detail">BAYVIEW HEIGHTS, WESTERN AUSTRALIA - 6099</div></div>
    </div>
    <div class="info" style="left:653px">
      <svg width="38" height="38" viewBox="0 0 38 38" fill="none" stroke="#c94fc0" stroke-width="3"><rect x="2" y="6" width="34" height="30"/><path d="M2 13h34" stroke-width="5"/><path d="M10 2v8M28 2v8M19 2v8"/></svg>
      <div><div class="info-title">BOOK NOW</div><div class="info-detail">0412 555 301 , 0468 555 927</div></div>
    </div>
  </div>
</header>

<section class="services">
  <div class="service is-current" style="left:105px"><div class="service-image is-colour" role="img" aria-label="Woman with long glossy copper hair"></div><span class="service-label">Hair</span></div>
  <div class="service" style="left:252px"><div class="service-image" role="img" aria-label="Lip gloss being applied with a brush"></div><span class="service-label">Make Up</span></div>
  <div class="service" style="left:399px"><div class="service-image" role="img" aria-label="Relaxing facial treatment"></div><span class="service-label">Facial</span></div>
  <div class="service" style="left:546px"><div class="service-image" role="img" aria-label="Back massage treatment"></div><span class="service-label">Massage</span></div>
  <div class="service" style="left:693px"><div class="service-image" role="img" aria-label="Manicured nails with dark polish"></div><span class="service-label">Nail</span></div>
  <div class="service" style="left:840px"><div class="service-image" role="img" aria-label="Warm wax being poured"></div><span class="service-label">Waxing</span></div>
</section>

<section class="price-list left">
  <span class="price-head" style="left:300px">APPRENTICE</span>
  <span class="price-head" style="left:379px">PRINCIPAL</span>
  <div class="price-row" style="top:42px"><span class="name">STYLING</span><span class="price" style="left:327px">25</span><span class="price" style="left:402px">40</span></div>
  <div class="price-row" style="top:88px"><span class="name">SILKA CURLS</span><span class="price" style="left:327px">35</span><span class="price" style="left:402px">50</span></div>
  <div class="price-row" style="top:133px"><span class="name">HAIR UP</span><span class="price" style="left:327px">35</span><span class="price" style="left:402px">60</span></div>
  <div class="price-row" style="top:179px"><span class="name">LADIES CUT</span><span class="price" style="left:327px">15</span><span class="price" style="left:402px">30</span></div>
  <div class="price-row" style="top:224px"><span class="name">CUT WITH BLOW DRY</span><span class="price" style="left:327px">25</span><span class="price" style="left:402px">40</span></div>
  <div class="price-row" style="top:270px"><span class="name">RESTYLE &amp; FINISH</span><span class="price" style="left:327px">30</span><span class="price" style="left:402px">50</span></div>
  <div class="price-row" style="top:316px"><span class="name">KIDS / MENS CUT</span><span class="price" style="left:327px">10</span><span class="price" style="left:402px">20</span></div>
</section>

<section class="price-list right">
  <span class="price-head" style="left:283px">APPRENTICE</span>
  <span class="price-head" style="left:363px">PRINCIPAL</span>
  <div class="price-row" style="top:42px"><span class="name">COLOUR - ROOTS</span><span class="price" style="left:310px">30</span><span class="price" style="left:386px">50</span></div>
  <div class="price-row" style="top:88px"><span class="name">EXTRA TINT OR TONER</span><span class="price" style="left:310px">20</span><span class="price" style="left:386px">20</span></div>
  <div class="price-row" style="top:133px"><span class="name">ADD FOILS 1/4 HEAD</span><span class="price" style="left:310px">20</span><span class="price" style="left:386px">30</span></div>
  <div class="price-row" style="top:179px"><span class="name">ADD FOILS 1/2 HEAD</span><span class="price" style="left:310px">40</span><span class="price" style="left:386px">60</span></div>
  <div class="price-row" style="top:224px"><span class="name">FULL HEAD FOILS</span><span class="price" style="left:310px">70</span><span class="price" style="left:386px">90</span></div>
  <div class="price-row" style="top:270px"><span class="name">PERM WITH CUT</span><span class="price" style="left:310px">60</span><span class="price" style="left:386px">80</span></div>
  <div class="price-row" style="top:316px"><span class="name">PERMA STRAIGHTENING</span><span class="price" style="left:310px">80</span><span class="price" style="left:388px">120</span></div>
</section>

<section class="testimonial">
  <div class="testimonial-image" role="img" aria-label="Woman with styled dark hair in a leafy garden setting"></div>
  <div class="testimonial-panel"></div>
</section>

</body>
</html>
```